REDESIGN MAIN BANNER IMAGE FOR MARKETING WEBSITE

I feel like my main banner image is too busy but I like it but i want to see other options. www.brightlanepromoworks.biz I want a nice professional clean design that goes with current theme of site. Must look professional and show the variety of incentives we offer but not be overwelming.

My business is called Brightlane Promo Works and I provide businesses around the world with marketing incentives that they can use to create exciting promotions and contest and marketing giveaways to help attract more customers.

I provide a variety of different types of incentives such as Vacation Certificates, Dining Vouchers, Hotel Savings Cards, Smart Watches, Etc. that businesses can use in their marketing efforts.

I want my main banner image to reflect the variety of different categories of incentives... that I offer here: https://www.brightlanepromoworks.biz/incentives

We can use images of certificates or images.....I just want the content to be the same:

CONTENT FOR MAIN BANNER IMAGE:
INCREASE LEADS AND SALES OVERNIGHT

CREATE EXCITING MARKETING PROMOTIONS GIVING AWAY SMART DEVICES, VACATION CERTIFICATES, DINING VOUCHERS AND OTHER INCENTIVES TO YOUR CUSTOMERS

GET A FREE SAMPLE PACKAGE FOR A LIMITED TIME ONLY

Target Market(s)

b2b business owners, ceo, president, owner, founder

Industry/Entity Type

Promotional

Requirements
Must have
• Hi guys keep in mind the finished product will have to be 1800x840

Nice to have
• I want a nice professional clean design that goes with current theme of site. Must look professional and show the variety of incentives we offer but not be overwelming.
Should not have

```html
<!DOCTYPE html>
<html lang="en">
<head>
<meta charset="utf-8">
<title>Brightlane Promo Works – Main Banner</title>
<link href="https://fonts.googleapis.com/css2?family=Krona+One&family=Oswald:wght@400;600&family=Roboto+Condensed:wght@400;700&display=swap" rel="stylesheet">
<style>
  :root{
    --blue-deep:#0b3f86;
    --blue-mid:#1a6fc0;
    --blue-light:#4fb3ea;
    --white:#ffffff;
    --green:#3f9e3c;
    --red:#d8121b;
    --red-dark:#a50d14;
    --ink:#222831;
    --grey:#5d6169;
    --paper-edge:#d9dbe0;
  }
  *{box-sizing:border-box;margin:0;padding:0}
  html,body{width:1200px;height:560px;overflow:hidden;background:var(--white)}
  .banner{position:relative;width:1200px;height:560px;overflow:hidden;background:var(--white);font-family:"Roboto Condensed",sans-serif}
  .backdrop{position:absolute;inset:0}

  .headline{position:absolute;left:25px;top:30px;font-family:"Krona One",sans-serif;font-weight:400;color:var(--white);font-size:36px;line-height:47px;letter-spacing:1px}
  .pitch{position:absolute;left:44px;top:366px;font-family:"Krona One",sans-serif;font-size:17.5px;line-height:21px;color:var(--red);
    -webkit-text-stroke:.5px var(--red-dark);
    text-shadow:1px 0 0 var(--white),-1px 0 0 var(--white),0 1px 0 var(--white),0 -1px 0 var(--white),1px 1px 0 var(--white),-1px -1px 0 var(--white),1px -1px 0 var(--white),-1px 1px 0 var(--white)}
  .offer{position:absolute;left:300px;width:620px;top:488px;text-align:center;font-family:"Krona One",sans-serif;color:var(--white);font-size:22px;line-height:30px}

  .shelf{position:absolute;inset:0}
  .flyer{position:absolute;display:flex;flex-direction:column;background:var(--white);transform-origin:right center;transform:perspective(900px) rotateY(-22deg);
    box-shadow:-4px 4px 10px rgba(0,0,0,.38);border-right:1px solid var(--paper-edge);overflow:hidden;color:var(--ink);padding:.7em .8em .6em}
  .fl-head{display:flex;align-items:flex-end;gap:.35em;font-family:"Oswald",sans-serif;line-height:1;flex:none}
  .fl-enjoy{font-size:3.4em;font-weight:400;color:var(--ink);letter-spacing:-.02em}
  .fl-tags{display:flex;flex-direction:column;gap:.15em;padding-bottom:.3em}
  .fl-pre{font-size:1em;color:var(--ink)}
  .fl-tag{background:var(--red);color:var(--white);font-size:1.6em;font-weight:600;padding:.05em .3em;align-self:flex-start}
  .fl-sub{font-family:"Oswald",sans-serif;font-size:1.1em;color:var(--ink);margin:.3em 0 .4em;line-height:1.2;flex:none}
  .fl-sub em{font-style:normal;color:var(--red)}
  .fl-photo{flex:1 1 0;min-height:20%;margin:0 -.8em;position:relative}
  .fl-band{flex:none;background:var(--red);color:var(--white);font-size:.85em;font-weight:700;padding:.55em .8em;margin:0 -.8em 0 -.8em;width:88%;border-top-right-radius:2em;border-bottom-right-radius:.4em;position:relative;z-index:1;margin-top:-.8em}
  .fl-copy{flex:none;font-size:.72em;color:var(--grey);margin:.45em 0;line-height:1.3}
  .fl-label{flex:none;align-self:flex-start;background:var(--red);color:var(--white);font-size:.75em;font-weight:700;padding:.2em .5em;margin:.25em 0 .15em;border-top-right-radius:.6em}
  .fl-list{flex:none;font-size:.66em;color:var(--grey);list-style:none;line-height:1.45;display:grid;grid-template-columns:1fr 1fr;column-gap:.6em}
  .fl-list li::before{content:"○ ";color:var(--ink)}
  .fl-cert{flex:none;display:flex;gap:.8em;align-items:center;border:1px solid #c9ccd2;border-radius:.7em;padding:.45em .6em;margin-top:.5em;box-shadow:0 1px 3px rgba(0,0,0,.15)}
  .fl-id{font-size:.64em;line-height:1.3;color:var(--ink);text-align:center;font-weight:700}
  .fl-id b{color:var(--red);display:block}
  .fl-url{font-size:.62em;text-align:center;line-height:1.3;flex:1;font-weight:700}
  .fl-url strong{color:var(--red);display:block;font-size:1.35em}
  .fl-url small{font-weight:400;display:block}
  .fl-ribbon{position:absolute;right:0;top:0;width:26%;padding:.6em .3em 1.4em;background:#eeeff1;text-align:center;font-family:"Oswald",sans-serif;color:var(--grey);line-height:1.1;
    clip-path:polygon(0 0,100% 0,100% 100%,50% 86%,0 100%);z-index:2}
  .fl-ribbon small{display:block;font-size:.75em}
  .fl-ribbon span{font-size:1.5em;font-weight:600}
  .fl-spots{position:absolute;right:-.9em;display:flex;flex-direction:column;gap:.9em;z-index:2}
  .fl-spot{width:5.6em;height:5.6em;border-radius:50%;border:.4em solid var(--red);box-shadow:0 0 0 .15em var(--white)}
</style>
</head>
<body>
<div class="banner">
  <svg class="backdrop" width="1200" height="560" viewBox="0 0 1200 560" aria-hidden="true">
    <defs>
      <linearGradient id="blueField" x1="0" y1="0" x2="1" y2="1">
        <stop offset="0" stop-color="#0a3576"/>
        <stop offset=".45" stop-color="#1d74c4"/>
        <stop offset="1" stop-color="#5cc0ee"/>
      </linearGradient>
      <linearGradient id="ray" x1="0" y1="0" x2="1" y2="0">
        <stop offset="0" stop-color="#ffffff" stop-opacity="0"/>
        <stop offset="1" stop-color="#ffffff" stop-opacity=".55"/>
      </linearGradient>
    </defs>
    <polygon points="0,0 560,0 300,340 0,560" fill="url(#blueField)"/>
    <polygon points="0,560 300,340 365,560" fill="#2f8fd6"/>
    <polygon points="180,0 560,0 300,340" fill="url(#ray)"/>
    <polygon points="0,230 300,340 0,420" fill="#ffffff" opacity=".18"/>
    <polygon points="120,560 300,340 230,560" fill="#ffffff" opacity=".35"/>
    <polygon points="300,340 1200,515 1200,560 362,560" fill="var(--green)"/>
  </svg>

  <h1 class="headline">INCREASE<br>LEADS AND<br>SALES<br>OVERNIGHT</h1>

  <p class="pitch">CREATE EXCITING MARKETING<br>PROMOTIONS GIVING AWAY SMART DEVICES,<br>VACATION CERTIFICATES, DINING VOUCHERS<br>AND OTHER INCENTIVES TO YOUR CUSTOMERS</p>

  <div class="shelf">
    <article class="flyer" style="left:386px;top:178px;width:92px;height:154px;font-size:3.6px">
      <div class="fl-head"><span class="fl-enjoy">YOUR</span><span class="fl-tags"><span class="fl-pre">HOTEL SAVINGS</span><span class="fl-tag">MEMBERSHIP</span></span></div>
      <p class="fl-sub">Savings Membership Card</p>
      <div class="fl-photo" role="img" aria-label="Photo of a pink piggy bank on a laptop" style="background:radial-gradient(circle at 45% 55%,#f2b6c6 0 22%,transparent 40%),linear-gradient(135deg,#cfd3d9,#9aa0a8 60%,#3c4047)"></div>
      <div class="fl-spots" style="top:34%">
        <div class="fl-spot" role="img" aria-label="Photo of a hotel lobby" style="background:linear-gradient(180deg,#b07a45,#3b2a1e)"></div>
        <div class="fl-spot" role="img" aria-label="Photo of a restaurant table" style="background:linear-gradient(180deg,#6d4b3a,#1f1a18)"></div>
      </div>
      <div class="fl-band">EXCLUSIVELY FOR : CUSTOMER NAME</div>
      <p class="fl-copy">Congratulations, you have been rewarded with this special offer. Visit the website below to redeem it today.</p>
      <span class="fl-label">FEATURES</span>
      <ul class="fl-list"><li>Hotel Savings Up To 50%</li><li>Dining Discounts</li><li>Shopping Rewards</li><li>Travel Perks</li></ul>
      <span class="fl-label">HOW CAN WE DO THIS?</span>
      <p class="fl-copy">Our partners fund this reward so you can enjoy it at no cost.</p>
      <span class="fl-label">WHAT OTHERS SAY</span>
      <p class="fl-copy">Customers love these rewards and return again.</p>
      <div class="fl-cert"><p class="fl-id">Certificate ID<b>#10983-95930</b></p><p class="fl-url">VIEW ALL THE DETAILS<strong>WWW.PERKVAULTOFFERS.COM</strong></p></div>
    </article>

    <article class="flyer" style="left:466px;top:150px;width:100px;height:206px;font-size:4.4px">
      <div class="fl-head"><span class="fl-enjoy">ENJOY</span><span class="fl-tags"><span class="fl-pre">7 DAYS</span><span class="fl-tag">LUXURY RESORT</span></span></div>
      <p class="fl-sub">7 Days Resort Stay</p>
      <div class="fl-photo" role="img" aria-label="Photo of a tropical resort by the sea" style="background:linear-gradient(180deg,#3f8fd6 0,#8cc6ef 35%,#e2c9a0 55%,#2a9bc0 75%,#176a94)"></div>
      <div class="fl-spots" style="top:38%">
        <div class="fl-spot" role="img" aria-label="Photo of a cruise ship" style="background:linear-gradient(180deg,#8fc8ef,#f2f2f2 55%,#2378b0)"></div>
        <div class="fl-spot" role="img" aria-label="Photo of a city at night" style="background:linear-gradient(180deg,#1b2240,#d98a2b)"></div>
      </div>
      <div class="fl-band">EXCLUSIVELY FOR : CUSTOMER NAME</div>
      <p class="fl-copy">Congratulations, you have been rewarded with this special offer. Visit the website below to redeem it today.</p>
      <span class="fl-label">FEATURES</span>
      <ul class="fl-list"><li>7 Days 6 Nights</li><li>Ocean View Rooms</li><li>Pool And Beach Access</li><li>Transferable Gift</li></ul>
      <span class="fl-label">HOW CAN WE DO THIS?</span>
      <p class="fl-copy">Our partners fund this reward so you can enjoy it at no cost.</p>
      <span class="fl-label">WHAT OTHERS SAY</span>
      <p class="fl-copy">Customers love these rewards and return again.</p>
      <div class="fl-cert"><p class="fl-id">Certificate ID<b>#10983-95930</b></p><p class="fl-url">VIEW ALL THE DETAILS<strong>WWW.PERKVAULTOFFERS.COM</strong></p></div>
    </article>

    <article class="flyer" style="left:558px;top:112px;width:102px;height:266px;font-size:5.2px">
      <div class="fl-head"><span class="fl-enjoy">ENJOY</span><span class="fl-tags"><span class="fl-pre">YOUR BRAND NEW</span><span class="fl-tag">SMARTWATCH</span></span></div>
      <p class="fl-sub">Take Control of Your Life With<br><em>Your New Smart Fitness Watch</em></p>
      <div class="fl-photo" role="img" aria-label="Photo of smart watches and a person exercising" style="background:radial-gradient(circle at 25% 60%,#1c1d20 0 18%,transparent 30%),linear-gradient(110deg,#4a4d52,#b5b8bd 50%,#eef0f2)"></div>
      <div class="fl-band">EXCLUSIVELY FOR : CUSTOMER NAME</div>
      <p class="fl-copy">Congratulations, you have been rewarded with this special offer. Visit the website below to redeem it today.</p>
      <span class="fl-label">FEATURES</span>
      <ul class="fl-list"><li>Heart Rate Monitor</li><li>Sleep Tracking</li><li>Step Counter</li><li>Waterproof Design</li></ul>
      <span class="fl-label">HOW CAN WE DO THIS?</span>
      <p class="fl-copy">Our partners fund this reward so you can enjoy it at no cost.</p>
      <span class="fl-label">WHAT OTHERS SAY</span>
      <p class="fl-copy">Customers love these rewards and return again.</p>
      <div class="fl-cert"><p class="fl-id">Certificate ID<b>#10983-95930</b>Expires 02/29/2020</p><p class="fl-url">VIEW ALL THE DETAILS<strong>WWW.PERKVAULTOFFERS.COM</strong></p></div>
    </article>

    <article class="flyer" style="left:650px;top:84px;width:128px;height:332px;font-size:6.4px">
      <div class="fl-head"><span class="fl-enjoy">ENJOY</span><span class="fl-tags"><span class="fl-pre">AIRFARE WITH</span><span class="fl-tag">HOTEL</span></span></div>
      <p class="fl-sub">Two Roundtrip Airfare with<br><em>2 Nights Hotel Accommodations</em></p>
      <div class="fl-photo" role="img" aria-label="Photo of an airliner flying above clouds" style="background:radial-gradient(ellipse at 60% 35%,#f5f7fa 0 12%,transparent 25%),linear-gradient(180deg,#2f74bd,#8dbfe8 55%,#eef3f9)"></div>
      <div class="fl-band">EXCLUSIVELY FOR : CUSTOMER NAME</div>
      <p class="fl-copy">Congratulations, you have been rewarded with this special offer. Visit the website below to redeem it today.</p>
      <span class="fl-label">FEATURES</span>
      <ul class="fl-list"><li>Two Roundtrip Tickets</li><li>2 Nights Hotel Stay</li><li>Choice Of Destinations</li><li>Transferable To Another Person</li></ul>
      <span class="fl-label">HOW CAN WE DO THIS?</span>
      <p class="fl-copy">Our partners fund this reward so you can enjoy it at no cost.</p>
      <span class="fl-label">WHAT OTHERS SAY</span>
      <p class="fl-copy">Customers love these rewards and return again.</p>
      <div class="fl-cert"><p class="fl-id">Certificate ID<b>#10983-95930</b>Expires 02/29/2020</p><p class="fl-url">VIEW ALL THE DETAILS OF THIS SPECIAL OFFER<strong>WWW.PERKVAULTOFFERS.COM</strong></p></div>
    </article>

    <article class="flyer" style="left:775px;top:52px;width:162px;height:424px;font-size:8px">
      <div class="fl-head"><span class="fl-enjoy">ENJOY</span><span class="fl-tags"><span class="fl-pre">A BOX OF WINE</span><span class="fl-tag">$100 OFF</span></span></div>
      <p class="fl-sub">Cases of 6, 12 or 15 bottles (750 ML)</p>
      <div class="fl-photo" role="img" aria-label="Photo of wine glasses, grapes and cheese" style="background:radial-gradient(circle at 25% 45%,#7a0f20 0 14%,transparent 24%),radial-gradient(circle at 60% 70%,#f0d37a 0 14%,transparent 26%),linear-gradient(160deg,#f1ece4,#c9b9a8 45%,#3f2b3a 80%,#2e3a22)"></div>
      <div class="fl-band">EXCLUSIVELY FOR : CUSTOMER NAME</div>
      <p class="fl-copy">Congratulations, you have been rewarded with this special offer. Visit the website below to redeem it today.</p>
      <span class="fl-label">FEATURES</span>
      <ul class="fl-list"><li>Full $100 Off Case Of Wine</li><li>Choice Of 6, 12 or 15 Bottles</li><li>Access To Exclusive Wines</li><li>No Cost To Redeem</li></ul>
      <span class="fl-label">HOW CAN WE DO THIS?</span>
      <p class="fl-copy">Our partners fund this reward so you can enjoy it at no cost.</p>
      <span class="fl-label">WHAT OTHERS SAY</span>
      <p class="fl-copy">Customers love these rewards and return again.</p>
      <div class="fl-cert"><p class="fl-id">Certificate ID<b>#10983-95930</b>Expires 02/29/2020</p><p class="fl-url">VIEW ALL THE DETAILS OF THIS SPECIAL OFFER<strong>WWW.PERKVAULTOFFERS.COM</strong><small>Terms and Conditions apply see website for details</small></p></div>
    </article>

    <article class="flyer" style="left:932px;top:16px;width:272px;height:524px;font-size:10.5px">
      <div class="fl-head"><span class="fl-enjoy">ENJOY</span><span class="fl-tags"><span class="fl-pre">BLUETOOTH PORTABLE</span><span class="fl-tag">SPEAKER</span></span></div>
      <p class="fl-sub">Bluetooth Portable<br><em>Speaker</em></p>
      <div class="fl-ribbon"><small>Compliments Of</small><span>LOGO</span><small>GOES HERE</small></div>
      <div class="fl-photo" role="img" aria-label="Photo of a blue portable speaker on a beach" style="background:radial-gradient(ellipse at 45% 60%,#1d5fa8 0 22%,transparent 34%),linear-gradient(180deg,#d8d2c6,#b7aa92 45%,#8f7f64 80%,#5d5140)"></div>
      <div class="fl-spots" style="top:40%">
        <div class="fl-spot" role="img" aria-label="Photo of people exercising outdoors" style="background:linear-gradient(180deg,#9cc3e3,#d3c3a5 60%,#7f6f55)"></div>
        <div class="fl-spot" role="img" aria-label="Photo of the speaker close up" style="background:linear-gradient(180deg,#2a6cb6,#0f3c72)"></div>
        <div class="fl-spot" role="img" aria-label="Photo of a hand holding the speaker" style="background:linear-gradient(180deg,#d9d9dc,#2a5fc0)"></div>
      </div>
      <div class="fl-band">EXCLUSIVELY FOR : CUSTOMER NAME</div>
      <p class="fl-copy" style="margin-right:26%">Congratulations, you have been rewarded with this special offer. Visit the website below to redeem it today.</p>
      <span class="fl-label">FEATURES</span>
      <ul class="fl-list" style="margin-right:24%"><li>Portable Waterproof Speaker</li><li>Full-Range Microphone</li><li>Support Memory Card</li><li>Bluetooth 5.0</li><li>12 Hours Play Time</li><li>Power Cable Included</li></ul>
      <span class="fl-label">HOW CAN WE DO THIS?</span>
      <p class="fl-copy" style="margin-right:24%">Our partners fund this reward so you can enjoy it at no cost.</p>
      <span class="fl-label">WHAT OTHERS SAY</span>
      <p class="fl-copy">Customers love these rewards and return again.</p>
      <div class="fl-cert"><p class="fl-id">Certificate ID<b>#10983-95930</b>Expires 02/29/2020</p><p class="fl-url">VIEW ALL THE DETAILS OF THIS SPECIAL OFFER AND REDEEM ONLINE AT<strong>WWW.PERKVAULTOFFERS.COM</strong><small>Terms and Conditions apply see website for details</small></p></div>
    </article>
  </div>

  <p class="offer">GET A FREE SAMPLE PACKAGE<br>FOR A LIMITED TIME ONLY</p>
</div>
</body>
</html>
```